Business Card Design

Im looking for a business card that will market/promote myself as in independent/freelancer in the beauty industry. Im looking for something very modern, and clean looking. no specific colors just something that doesnt look cheesy, would like a very professional look

Industry/Entity Type

Business

Contact Information for Business Card

Corinne Baldasso, Hairstylist(Cut, color, blowdry, style, extensions, straightening treatments), makeup artist, red carpet, in-salon, editorial, tv, film, contact is 5073914620 cbstyling@quillmail.net, LA based

```html
<!DOCTYPE html>
<html lang="en">
<head>
<meta charset="UTF-8">
<title>Corinne Baldasso – Business Card</title>
<link rel="stylesheet" href="https://fonts.googleapis.com/css2?family=Arimo:wght@700&display=swap">
<style>
  :root {
    --card-yellow: #eeff12;
    --edge-shade: rgba(70, 70, 0, 0.85);
    --card-black: #060807;
    --text-yellow: #f2f70a;
  }
  html, body {
    margin: 0;
    padding: 0;
    width: 1200px;
    height: 720px;
    overflow: hidden;
    background: var(--card-black);
  }
  .card {
    position: relative;
    width: 1200px;
    height: 720px;
    display: flex;
  }
  .side-band {
    background: var(--card-yellow);
    box-shadow: inset 0 0 26px 6px var(--edge-shade);
  }
  .side-band--left { width: 312px; }
  .side-band--right { width: 323px; }
  .center-panel {
    position: relative;
    flex: 1;
    background: var(--card-black);
  }
  .identity {
    position: absolute;
    left: 210px;
    top: 238px;
    margin: 0;
    font-family: "Arimo", Arial, sans-serif;
    font-weight: 700;
    font-size: 35px;
    line-height: 1;
    color: var(--text-yellow);
  }
  .identity__line {
    display: block;
    margin-bottom: 56px;
  }
</style>
</head>
<body>
  <div class="card">
    <div class="side-band side-band--left"></div>
    <div class="center-panel">
      <p class="identity">
        <span class="identity__line">Corinne</span>
        <span class="identity__line">Baldasso</span>
        <span class="identity__line">Hairstylist</span>
      </p>
    </div>
    <div class="side-band side-band--right"></div>
  </div>
</body>
</html>
```